Business Card Design Project

Business card for new event planning company. I will load in 2 different colors of logs for you to use.

Target Market(s)

meeting planners and business leaders

Industry/Entity Type

Event Planning

Requirements
Must have
• memorable/ creative please - maybe logo on back of the card

Information for business card: (Information may change)

LaVonna Birchwell
lav@MarigoldOccasionsandGatherings.com
www.MarigoldOccasionsandGatherings.com
555.730.2964
Nice to have
• Do you think it would be too much to add twiiter, FB, linked in logo to card to connect?

all are LaVonna Birchwell

```html
<!DOCTYPE html>
<html lang="en">
<head>
<meta charset="utf-8">
<title>Marigold Occasions &amp; Gatherings – Business Card</title>
<link href="https://fonts.googleapis.com/css2?family=Oswald:wght@300;400;500&display=swap" rel="stylesheet">
<style>
  :root {
    --backdrop: #e9e8ec;
    --card-white: #fbfbfb;
    --brand-purple: #6c56a6;
    --brand-purple-light: #7a65b3;
    --band-red: #e0231c;
    --band-red-dark: #b8140f;
    --ink-white: #ffffff;
    --ink-soft: rgba(255,255,255,0.78);
    --divider: rgba(255,255,255,0.35);
  }
  * { box-sizing: border-box; margin: 0; padding: 0; }
  html, body {
    width: 1200px; height: 900px; overflow: hidden;
    background: var(--backdrop);
    font-family: "Oswald", "Arial Narrow", sans-serif;
  }
  .canvas { position: relative; width: 1200px; height: 900px; }

  .card {
    position: absolute; left: 250px; width: 700px; height: 400px;
    border-radius: 4px;
    box-shadow: 0 10px 28px rgba(40,30,60,0.18);
    overflow: hidden;
  }

  /* Logo side */
  .card--logo { top: 40px; background: var(--card-white); }
  .logo-lockup {
    position: absolute; top: 92px; left: 0; right: 0;
    display: flex; align-items: center; justify-content: center; gap: 22px;
    color: var(--brand-purple); font-weight: 400;
  }
  .logo-lockup__dot {
    width: 46px; height: 46px; border-radius: 50%;
    background: var(--brand-purple);
  }
  .logo-lockup__name { line-height: 1; }
  .logo-lockup__main { display: block; font-size: 74px; letter-spacing: 2px; }
  .logo-lockup__sub { display: block; font-size: 22px; letter-spacing: 1px; margin-top: 4px; text-align: right; }

  .web-band {
    position: absolute; left: 0; right: 0; top: 276px; height: 50px;
    background: var(--band-red);
    border-top: 3px solid var(--band-red-dark);
    border-bottom: 3px solid var(--band-red-dark);
    display: flex; align-items: center; justify-content: center;
    color: var(--ink-white); font-weight: 500; font-size: 22px; letter-spacing: 1.5px;
  }

  /* Contact side */
  .card--contact {
    top: 470px;
    background: linear-gradient(135deg, var(--brand-purple-light), var(--brand-purple));
    color: var(--ink-white);
  }
  .contact-logo {
    position: absolute; left: 50px; top: 118px; width: 250px;
    display: flex; align-items: center; gap: 14px; font-weight: 400;
  }
  .contact-logo__dot { width: 28px; height: 28px; border-radius: 50%; background: var(--ink-white); flex: none; }
  .contact-logo__main { display: block; font-size: 40px; letter-spacing: 1px; line-height: 1; }
  .contact-logo__sub { display: block; font-size: 13px; margin-top: 3px; }

  .divider {
    position: absolute; left: 318px; top: 70px; width: 1px; height: 160px;
    background: var(--divider);
  }
  .contact-details { position: absolute; left: 345px; top: 78px; right: 20px; }
  .contact-details__name { font-size: 26px; font-weight: 400; letter-spacing: 0.5px; margin-bottom: 22px; }
  .contact-line {
    display: flex; align-items: center; gap: 12px;
    font-size: 16px; font-weight: 300; color: var(--ink-white);
    margin-bottom: 14px; white-space: nowrap;
  }
  .contact-line svg { width: 16px; height: 16px; flex: none; fill: var(--ink-white); }
</style>
</head>
<body>
<main class="canvas">

  <section class="card card--logo" aria-label="Card back">
    <div class="logo-lockup">
      <span class="logo-lockup__name">
        <span class="logo-lockup__main">MARIGOLD</span>
        <span class="logo-lockup__sub">Occasions&amp;Gatherings</span>
      </span>
      <span class="logo-lockup__dot"></span>
    </div>
    <div class="web-band">WWW.MARIGOLDOCCASIONSANDGATHERINGS.COM</div>
  </section>

  <section class="card card--contact" aria-label="Card front">
    <div class="contact-logo">
      <span>
        <span class="contact-logo__main">MARIGOLD</span>
        <span class="contact-logo__sub">Occasions&amp;Gatherings</span>
      </span>
      <span class="contact-logo__dot"></span>
    </div>
    <div class="divider"></div>
    <div class="contact-details">
      <p class="contact-details__name">LaVonna Birchwell</p>
      <p class="contact-line">
        <svg viewBox="0 0 24 24" aria-hidden="true"><path d="M6.6 10.8c1.4 2.8 3.8 5.1 6.6 6.6l2.2-2.2c.3-.3.7-.4 1-.2 1.1.4 2.3.6 3.6.6.6 0 1 .4 1 1V20c0 .6-.4 1-1 1C10.6 21 3 13.4 3 4c0-.6.4-1 1-1h3.5c.6 0 1 .4 1 1 0 1.3.2 2.5.6 3.6.1.3 0 .7-.2 1l-2.3 2.2z"/></svg>
        555.730.2964
      </p>
      <p class="contact-line">
        <svg viewBox="0 0 24 24" aria-hidden="true"><path d="M2 5h20v14H2V5zm2 2v.5l8 5 8-5V7H4zm0 2.8V17h16V9.8l-8 5-8-5z"/></svg>
        lav@MarigoldOccasionsandGatherings.com
      </p>
      <p class="contact-line">
        <svg viewBox="0 0 24 24" aria-hidden="true"><path d="M12 2a10 10 0 100 20 10 10 0 000-20zm6.9 9h-3a15 15 0 00-1.2-5.5A8 8 0 0118.9 11zM12 4c.9 1.2 1.8 3.6 1.9 7h-3.8c.1-3.4 1-5.8 1.9-7zM9.3 5.5A15 15 0 008.1 11h-3a8 8 0 014.2-5.5zM5.1 13h3a15 15 0 001.2 5.5A8 8 0 015.1 13zm6.9 7c-.9-1.2-1.8-3.6-1.9-7h3.8c-.1 3.4-1 5.8-1.9 7zm2.7-1.5a15 15 0 001.2-5.5h3a8 8 0 01-4.2 5.5z"/></svg>
        www.MarigoldOccasionsandGatherings.com
      </p>
    </div>
  </section>

</main>
</body>
</html>
```